Verdo Studios Business Card

Business card for video production company, I want to give the impression of quality, It has to stand out for its design; it has to be easily readable and please avoid any extravaganza!. I'm looking for a first impression, then the card goes to the trash.

You guys have complete freedom of design! background color, logo colors etc
you can choose one side card or two sided, die cut also a possibility .
Just let me know for what kind of card is your design.
In the files you will find the logo .ai to modify it.

One of the differences between the ambiguous terms Filmmaker and videographer is that filmmaking is more arty, we tend to leave backgrounds out of focus, we create different layers or points of attention with our lens.

Logo
Filmmaking Done Right
www.verdostudios-example.com
www.socialpage-example.com/verdostudios
tomas@verdostudios-example.com
555-318-6092
Add QR Code

```html
<!DOCTYPE html>
<html lang="en">
<head>
<meta charset="utf-8">
<title>Verdo Studios Business Card</title>
<link rel="stylesheet" href="https://fonts.googleapis.com/css2?family=Michroma&family=Arimo:wght@400;700&display=swap">
<style>
  :root {
    --stage: #2a2a2c;
    --brand-green: #6abf45;
    --card-black: #0f0f10;
    --ink-white: #ffffff;
    --ink-grey: #c9c9c9;
    --ink-faint: #222224;
  }
  html, body {
    margin: 0;
    padding: 0;
    overflow: hidden;
  }
  .canvas {
    position: relative;
    width: 1200px;
    height: 1000px;
    background: var(--stage);
    overflow: hidden;
  }
  .card-shapes {
    position: absolute;
    inset: 0;
  }
  .front-name {
    position: absolute;
    left: 100px;
    top: 275px;
    width: 460px;
    text-align: center;
    font-family: "Michroma", sans-serif;
    font-size: 28px;
    line-height: 40px;
    letter-spacing: 1px;
    color: var(--ink-white);
    text-transform: uppercase;
  }
  .back-details {
    position: absolute;
    right: 165px;
    top: 565px;
    text-align: right;
    font-family: "Arimo", sans-serif;
    color: var(--ink-grey);
    font-size: 14px;
    line-height: 24px;
  }
  .tagline {
    font-weight: 700;
    font-size: 18px;
    color: var(--brand-green);
    margin: 0 0 14px;
  }
  .contact-line {
    margin: 0;
  }
  .back-faint-name {
    position: absolute;
    left: 630px;
    top: 762px;
    font-family: "Michroma", sans-serif;
    font-size: 20px;
    color: var(--ink-faint);
    text-transform: uppercase;
  }
</style>
</head>
<body>
<main class="canvas">
  <svg class="card-shapes" width="1200" height="1000" viewBox="0 0 1200 1000" aria-hidden="true">
    <g class="card-front" fill="#6abf45" stroke="#6abf45">
      <rect x="100" y="150" width="460" height="290" rx="40" stroke="none"/>
      <polygon points="530,295 790,140 790,450" stroke-width="30" stroke-linejoin="round"/>
    </g>
    <g class="card-back" fill="#0f0f10" stroke="#0f0f10">
      <rect x="600" y="530" width="460" height="290" rx="40" stroke="none"/>
      <polygon points="630,675 380,520 380,830" stroke-width="30" stroke-linejoin="round"/>
    </g>
  </svg>

  <div class="front-name">Verdo Studios</div>

  <section class="back-details">
    <p class="tagline">Filmmaking Done Right</p>
    <p class="contact-line">Email : tomas@verdostudios-example.com</p>
    <p class="contact-line">M : 555-318-6092</p>
    <p class="contact-line">www.socialpage-example.com/verdostudios</p>
    <p class="contact-line">www.verdostudios-example.com</p>
    <p class="contact-line">add qr code</p>
  </section>

  <div class="back-faint-name">Verdo Studios</div>
</main>
</body>
</html>
```